Business Card Design

It is an assisted living facility. I wanted the name to reflect that we are a step above other facilities; i.e., professionally decorated rooms, cloth napkins, family dinners, etc. My motto is: COME WHERE YOU ARE CELEBRATED! Also, I have thought about having a house held with the "Hands" and the motto around it but I have seen that logo used other places. In other words, HELP!

I do not have a photo yet, but the photographer is coming next week. I would like the back of the card to have a picture of the facility.

Industry/Entity Type

Business

Contact Information for Business Card

BRIGHT MEADOW ASSISTED LIVING, LLC, 2938 Quillmont Dr., FL 33482-7261
Phone: (555) 214-6037; Fax: (555)
Linda Pruett, Owner/Administrator

```html
<!DOCTYPE html>
<html lang="en">
<head>
<meta charset="utf-8">
<title>Bright Meadow Assisted Living – Business Card</title>
<link rel="stylesheet" href="https://fonts.googleapis.com/css2?family=Oswald:wght@600;700&family=Arimo:wght@400;700&display=swap">
<style>
  :root {
    --backdrop: #eceeee;
    --leaf-green: #67b833;
    --charcoal: #333232;
    --amber: #f6a312;
    --white: #ffffff;
    --ink: #1d1d1d;
  }
  * { margin: 0; padding: 0; box-sizing: border-box; }
  html, body {
    width: 1200px; height: 805px; overflow: hidden;
    background: var(--backdrop);
  }
  .card {
    position: absolute; left: 116px; top: 124px;
    width: 957px; height: 565px;
    background: var(--leaf-green);
    overflow: hidden;
    box-shadow: 0 4px 14px rgba(0,0,0,0.18);
  }
  .card-shapes { position: absolute; inset: 0; }
  .motto {
    position: absolute; left: 0; right: 0; top: 34px;
    text-align: center;
    font-family: 'Oswald', sans-serif; font-weight: 700;
    font-size: 58px; line-height: 1; letter-spacing: 0.5px;
    color: var(--white);
    -webkit-text-stroke: 2px var(--ink);
    paint-order: stroke fill;
    text-shadow: 3px 3px 0 var(--ink);
    transform: scaleY(1.05);
  }
  .contact {
    position: absolute; right: 85px; top: 192px;
    text-align: right;
    font-family: 'Arimo', sans-serif; color: var(--white);
  }
  .contact-name { font-size: 28px; font-weight: 700; line-height: 36px; }
  .contact-role { font-size: 26px; line-height: 36px; margin-bottom: 24px; }
  .contact-line {
    display: flex; justify-content: flex-end; align-items: center;
    gap: 6px; font-size: 23px; height: 51px;
  }
  .contact-line svg { width: 28px; height: 28px; fill: var(--amber); }
  .brand-name {
    position: absolute; left: 108px; top: 455px;
    font-family: 'Oswald', sans-serif; font-weight: 600;
    font-size: 30px; line-height: 42px;
    color: var(--amber);
  }
</style>
</head>
<body>
  <section class="card">
    <svg class="card-shapes" viewBox="0 0 957 565" width="957" height="565" aria-hidden="true">
      <path fill="var(--amber)" d="M0,160 C90,188 180,220 200,262 C215,200 260,128 480,116 C700,108 860,128 957,138 L957,565 L0,565 Z"/>
      <path fill="var(--charcoal)" d="M0,172 C90,200 180,232 200,275 C215,212 260,140 480,128 C700,120 860,140 957,150 L957,565 L0,565 Z"/>
    </svg>

    <h1 class="motto">COME WHERE YOU ARE CELEBRATED!</h1>

    <div class="contact">
      <p class="contact-name">Linda Pruett</p>
      <p class="contact-role">Owner/Administrator</p>
      <p class="contact-line">
        <svg viewBox="0 0 24 24" aria-label="Phone"><path d="M6.6 10.8a15.1 15.1 0 0 0 6.6 6.6l2.2-2.2c.3-.3.7-.4 1-.2 1.1.4 2.3.6 3.6.6.6 0 1 .4 1 1V20c0 .6-.4 1-1 1A17 17 0 0 1 3 4c0-.6.4-1 1-1h3.5c.6 0 1 .4 1 1 0 1.3.2 2.5.6 3.6.1.3 0 .7-.2 1z"/></svg>
        <span>(555) 214-6037</span>
      </p>
      <p class="contact-line">
        <svg viewBox="0 0 24 24" aria-label="Fax"><path d="M7 2h10v6H7zM3 9h18v11H3zm3 3v2h12v-2zm0 4v2h12v-2z"/></svg>
        <span>(555)</span>
      </p>
      <p class="contact-line">
        <svg viewBox="0 0 24 24" aria-label="Address"><path d="M12 2a7 7 0 0 0-7 7c0 5 7 13 7 13s7-8 7-13a7 7 0 0 0-7-7zm0 9.5A2.5 2.5 0 1 1 12 6.5a2.5 2.5 0 0 1 0 5z"/></svg>
        <span>2938 Quillmont Dr., FL 33482-7261</span>
      </p>
    </div>

    <p class="brand-name">BRIGHT MEADOW<br>ASSISTED LIVING</p>
  </section>
</body>
</html>
```